label design for oral care product

Kindly invite you to design bottle label (114 mm*40 mm) for our product, a kind of oral care product. The GEL is different from our previous cleanser product, as the pic we uploaded for demonstration. The color of frosted glass bottle is dark green, but the cap is white. You could download the pic of bottle among the uploaded files. The logo file and label content description are attached too. Please check them. Our product is made from many kinds of natural plant extracts, which includes herb and fruit. I wish the label would make our product look high-end and reliable. And it would be better if you could give some advice on paper material and special requirements for printing, related to your design. I value the texture of label too, because I think that stands for the quality of products. No color limitation for the use of our logo.
Target Market(s)
20-40 female, who value oral health.
Colors
Designer to choose colors to be used in the design.
Look and feel
Each slider illustrates characteristics of the customer's brand and the style your logo design should communicate.

```html
<!DOCTYPE html>
<html lang="en">
<head>
<meta charset="utf-8">
<title>Aligner Gel – Bottle Label</title>
<link rel="stylesheet" href="https://fonts.googleapis.com/css2?family=Roboto:wght@400;500;700&family=Roboto+Condensed:wght@500;700;800&display=swap">
<style>
  :root {
    --backdrop: #3a3a3c;
    --label-white: #ffffff;
    --band-grey: #404042;
    --band-grey-light: #6a6a6c;
    --brand-black: #231f20;
    --accent-blue: #1e9be0;
    --accent-blue-dark: #0b5fae;
    --accent-blue-light: #5cc3f0;
    --ink-dark: #2b2b2b;
  }
  html, body {
    margin: 0;
    padding: 0;
    width: 1025px;
    height: 1200px;
    overflow: hidden;
    background: var(--backdrop);
  }
  .canvas {
    position: relative;
    width: 1025px;
    height: 1200px;
  }
  .label {
    position: absolute;
    left: 40px;
    top: 434px;
    width: 945px;
    height: 331px;
    display: block;
  }
  .label-body { fill: var(--label-white); }
  .grey-band { fill: url(#bandShade); }
  .blue-stripe { fill: url(#stripeBlue); }
  .blue-panel { fill: url(#panelBlue); }
  .brand-block { fill: var(--brand-black); }
  .brand-name {
    font-family: "Roboto", sans-serif;
    font-weight: 700;
    font-size: 38px;
    fill: var(--label-white);
  }
  .brand-dot { fill: var(--label-white); }
  .product-title {
    font-family: "Roboto Condensed", sans-serif;
    font-weight: 800;
    font-size: 74px;
    fill: var(--brand-black);
    stroke: var(--accent-blue);
    stroke-width: 10px;
    stroke-linejoin: round;
    paint-order: stroke fill;
  }
  .tagline {
    font-family: "Roboto Condensed", sans-serif;
    font-weight: 500;
    font-size: 22px;
    fill: var(--label-white);
  }
  .claim {
    font-family: "Roboto Condensed", sans-serif;
    font-weight: 700;
    font-size: 22px;
    fill: var(--label-white);
  }
  .volume {
    font-family: "Roboto", sans-serif;
    font-weight: 700;
    font-size: 18px;
    fill: var(--ink-dark);
  }
  .section-head {
    font-family: "Roboto", sans-serif;
    font-weight: 700;
    font-size: 21px;
  }
  .section-text {
    font-family: "Roboto", sans-serif;
    font-weight: 400;
    font-size: 21px;
  }
  .ingredients { fill: var(--ink-dark); }
  .directions { fill: var(--label-white); }
</style>
</head>
<body>
<div class="canvas">
  <svg class="label" viewBox="0 0 1270 445" xmlns="http://www.w3.org/2000/svg" role="img" aria-label="Aligner Gel bottle label">
    <defs>
      <clipPath id="labelShape">
        <rect x="0" y="0" width="1270" height="445" rx="42" ry="42"/>
      </clipPath>
      <linearGradient id="bandShade" x1="0" y1="0" x2="1" y2="0">
        <stop offset="0" stop-color="#3c3c3e"/>
        <stop offset="0.45" stop-color="#5a5a5c"/>
        <stop offset="0.7" stop-color="#3e3e40"/>
        <stop offset="1" stop-color="#39393b"/>
      </linearGradient>
      <linearGradient id="stripeBlue" x1="0" y1="0" x2="1" y2="0">
        <stop offset="0" stop-color="#ffffff"/>
        <stop offset="0.25" stop-color="var(--accent-blue)"/>
        <stop offset="1" stop-color="var(--accent-blue-dark)"/>
      </linearGradient>
      <linearGradient id="panelBlue" x1="0" y1="0" x2="1" y2="1">
        <stop offset="0" stop-color="var(--accent-blue-light)"/>
        <stop offset="1" stop-color="#1a86cc"/>
      </linearGradient>
      <linearGradient id="whiteFade" x1="0" y1="0" x2="1" y2="0">
        <stop offset="0" stop-color="#ffffff" stop-opacity="1"/>
        <stop offset="0.5" stop-color="#ffffff" stop-opacity="0"/>
      </linearGradient>
    </defs>

    <g clip-path="url(#labelShape)">
      <rect class="label-body" x="0" y="0" width="1270" height="445"/>

      <!-- diagonal grey band -->
      <polygon class="grey-band" points="0,358 1270,42 1270,388 0,388"/>
      <polygon fill="url(#whiteFade)" points="0,345 760,160 0,362"/>

      <!-- blue accent stripe -->
      <polygon class="blue-stripe" points="0,350 1270,4 1270,46 0,362"/>

      <!-- blue block, lower left -->
      <rect class="blue-panel" x="84" y="298" width="241" height="112"/>

      <!-- brand block -->
      <polygon class="brand-block" points="510,0 762,0 762,133 510,182"/>
      <text class="brand-name" x="622" y="80" text-anchor="middle">Brisk</text>
      <text class="brand-name" x="622" y="120" text-anchor="middle">Bloom</text>
      <circle class="brand-dot" cx="706" cy="106" r="8"/>

      <!-- product naming -->
      <text class="product-title" x="635" y="240" text-anchor="middle">Aligner Gel</text>
      <text class="tagline" x="635" y="298" text-anchor="middle">Immune Support for Oral Health</text>
      <text class="claim" x="635" y="340" text-anchor="middle">Solution to Maintain Dental</text>
      <text class="claim" x="635" y="367" text-anchor="middle">Hygiene and Strengthen Gums</text>

      <text class="volume" x="635" y="420" text-anchor="middle">30 ml / 1 fl oz</text>

      <!-- ingredients -->
      <g class="ingredients" text-anchor="middle">
        <text class="section-head" x="205" y="60">CONTAINS:</text>
        <text class="section-text" x="205" y="89">a proprietary blend of</text>
        <text class="section-text" x="205" y="117">natural plant extract</text>
        <text class="section-text" x="205" y="145">including Angelica, Radix</text>
        <text class="section-text" x="205" y="174">Rehmanniae, Coptis,</text>
        <text class="section-text" x="205" y="202">Honeysuckle, Echinacea,</text>
        <text class="section-text" x="205" y="230">Sage, Chamomile,</text>
        <text class="section-text" x="205" y="258">Acerola cherry.</text>
      </g>

      <!-- directions -->
      <g class="directions" text-anchor="middle">
        <text class="section-head" x="1077" y="177">DIRECTIONS:</text>
        <text class="section-text" x="1077" y="218">Drop on the teeth</text>
        <text class="section-text" x="1077" y="246">directly after brushing.</text>
        <text class="section-text" x="1077" y="274">Or, put into clear</text>
        <text class="section-text" x="1077" y="303">aligners before wearing</text>
        <text class="section-text" x="1077" y="331">again. No need to rinse</text>
        <text class="section-text" x="1077" y="359">your mouth with water.</text>
      </g>
    </g>
  </svg>
</div>
</body>
</html>
```